Medical Advertising Website Design
website redesign
Medical Advertising Website Design - Advertising
Creative Brief
Advertising
http://www.kvmedlink.example/
K&V medlink is an ad agency with 100% focus on healthcare (pharmaceutical company) clients. Here is copy for the open web page which gives an overview--
K&V MEDLINK COMMUNICATIONS
YOUR STRATEGIC PARTNER
[GLOBAL HEADLINE]
Raising Strategic Partnership to a Higher Level
TABS
Who We Are
Our Approach
What We Do
Therapeutic Experience
Our Work
Contact Us
At K&V our clients are our partners. We believe that being a great partner means going beyond the expected to bring value through the superior customer experience.
• Strong Key Opinion Leader relationships
• Specialized in “high science” markets
• Industry side experience… “We’ve sat in your chair”
• Superior program financial management
• A leader in managing today’s increased compliance requirements
[Subhead]
Our Mission
“Our customer service mission is to develop superior client relationships built on a mutual trust and a strategic partnership. This partnership is built through our superior industry knowledge, clear understanding of client objectives and expectations, and from the extraordinary value K&V provides beyond the programs we deliver. Our excellence is defined by unwavering quality of work, attention to detail, consistent/timely communications, flexibility to change, and through fair and reasonable pricing. Ultimately, it is our commitment to these values that result in anticipating and exceeding our clients expectations.”
Likes - unique yet professional, clean, crisp design Dislikes - bland, boring appearance. Clutter. Lack of flow. No Flash as iPads / iPhones can't read them.
Service Oriented
PMS 301
bright greens like PMS 362
maybe orange/yellow oranges for emphasis
below header
Company emphasis is strategic partnership for all of their clients

```html
<!DOCTYPE html>
<html lang="en">
<head>
<meta charset="utf-8">
<title>K&amp;V Medlink</title>
<link href="https://fonts.googleapis.com/css2?family=Arimo:wght@400;700&display=swap" rel="stylesheet">
<style>
  :root {
    --brand-blue: #0b5394;
    --nav-blue: #0a4f8f;
    --nav-dark: #083f73;
    --sky-band: #c9dced;
    --text-grey: #6b6b6b;
    --panel-top: #f4f4f4;
    --panel-bottom: #d9d9d9;
    --rule: #c8c8c8;
    --white: #ffffff;
  }
  * { box-sizing: border-box; margin: 0; padding: 0; }
  html, body { width: 1200px; height: 923px; overflow: hidden; }
  body {
    position: relative;
    background: var(--white);
    font-family: "Arimo", Arial, sans-serif;
    color: var(--text-grey);
  }
  .side-band { position: absolute; top: 170px; height: 255px; background: var(--sky-band); }
  .side-band.left { left: 0; width: 155px; }
  .side-band.right { right: 0; width: 147px; }

  .brand {
    position: absolute; left: 155px; top: 44px;
    display: flex; align-items: center; gap: 12px;
  }
  .brand-mark { width: 26px; height: 26px; border-radius: 50%; background: var(--brand-blue); flex: none; }
  .brand-name { color: var(--brand-blue); font-weight: 700; font-size: 22px; letter-spacing: 0.5px; }

  .account-links {
    position: absolute; top: 48px; left: 830px;
    display: flex; gap: 34px; font-size: 12px; color: var(--brand-blue);
  }
  .account-links span { display: flex; align-items: center; gap: 8px; }
  .account-links svg { width: 22px; height: 22px; }

  .hero {
    position: absolute; left: 155px; top: 137px; width: 898px; height: 217px;
    background: radial-gradient(ellipse at 50% 70%, #b9c7d4 0%, #e4e9ee 45%, #ffffff 80%);
  }

  .main-nav {
    position: absolute; left: 155px; top: 354px; width: 898px; height: 40px;
    background: linear-gradient(var(--nav-blue), var(--nav-dark));
    display: flex; justify-content: space-around; align-items: center;
    border-radius: 4px 4px 0 0;
  }
  .main-nav a {
    color: var(--white); text-decoration: none; font-size: 12px;
    text-align: center; line-height: 1.05; position: relative;
  }
  .main-nav a.active::after {
    content: ""; position: absolute; left: 50%; top: 24px; margin-left: -10px;
    border: 10px solid transparent; border-top-color: var(--nav-dark); border-bottom: 0;
  }

  .content-panel {
    position: absolute; left: 155px; top: 394px; width: 898px; height: 409px;
    background: linear-gradient(var(--panel-top), var(--panel-bottom));
    box-shadow: 0 4px 10px rgba(0,0,0,0.25);
  }
  .home-icon { position: absolute; left: 20px; top: 28px; width: 22px; height: 20px; }
  .search {
    position: absolute; left: 693px; top: 25px; width: 167px; height: 28px;
    display: flex; border: 1px solid var(--nav-blue); background: var(--white);
  }
  .search-btn { width: 38px; background: var(--nav-blue); display: flex; align-items: center; justify-content: center; }
  .search-field { flex: 1; font-size: 11px; color: #9a9a9a; display: flex; align-items: center; justify-content: center; }
  .panel-rule { position: absolute; left: 20px; right: 20px; top: 60px; border-top: 1px solid var(--rule); }

  .intro { position: absolute; left: 35px; top: 94px; width: 830px; font-size: 11px; line-height: 22.5px; text-transform: uppercase; }
  .intro ul { list-style: none; }
  .mission-title { color: var(--brand-blue); font-size: 17px; font-weight: 700; margin-top: 22px; line-height: 20px; }
  .mission-text { font-size: 11px; line-height: 21px; margin-top: 4px; }

  .copyright {
    position: absolute; top: 843px; width: 100%; text-align: center;
    font-size: 11px; color: var(--brand-blue);
  }
  .site-footer {
    position: absolute; left: 155px; top: 873px; width: 898px; height: 50px;
    background: var(--nav-dark);
    display: flex; justify-content: center; align-items: center; gap: 44px;
    color: var(--white); font-size: 11px;
  }
</style>
</head>
<body>
  <div class="side-band left"></div>
  <div class="side-band right"></div>

  <header class="brand">
    <span class="brand-mark"></span>
    <span class="brand-name">K&amp;V MEDLINK</span>
  </header>

  <nav class="account-links">
    <span><svg viewBox="0 0 22 22"><circle cx="11" cy="11" r="10" fill="#0b5394"/><rect x="9.5" y="9" width="3" height="8" fill="#fff"/><circle cx="11" cy="6" r="1.7" fill="#fff"/></svg>LOGIN</span>
    <span><svg viewBox="0 0 22 22"><circle cx="11" cy="11" r="10" fill="#0b5394"/><path d="M6 15l1-3 7-7 2 2-7 7z" fill="#fff"/></svg>REGISTER</span>
  </nav>

  <div class="hero" role="img" aria-label="Group photo of smiling doctors and nurses in white coats and scrubs"></div>

  <nav class="main-nav">
    <a class="active">HOME</a>
    <a>WHO WE ARE</a>
    <a>OUR APPROACH</a>
    <a>WHAT WE DO</a>
    <a>THERAPEUTIC<br>EXPERIENCE</a>
    <a>OUR WORK</a>
    <a>CONTACT US</a>
  </nav>

  <main class="content-panel">
    <svg class="home-icon" viewBox="0 0 22 20"><path d="M11 1L1 10h3v9h5v-6h4v6h5v-9h3z" fill="#6b6b6b"/></svg>
    <div class="search">
      <div class="search-btn"><svg width="16" height="16" viewBox="0 0 16 16"><circle cx="9.5" cy="6.5" r="4.5" fill="none" stroke="#fff" stroke-width="2"/><path d="M6.5 9.5L2 14" stroke="#fff" stroke-width="2.5"/></svg></div>
      <div class="search-field">SEARCH</div>
    </div>
    <div class="panel-rule"></div>

    <section class="intro">
      <p>A full service medical education agency that goes beyond the expected:</p>
      <ul>
        <li>• Strategically focused</li>
        <li>• Customer service oriented</li>
        <li>• Compliance leadership</li>
      </ul>
      <h2 class="mission-title">OUR MISSION</h2>
      <p class="mission-text">Our customer service mission is to develop superior client relationships built on a mutual trust and a strategic partnership. This partnership is built through our superior industry knowledge, clear understanding of client objectives and expectations, and from the extraordinary value K&amp;V provides beyond the programs we deliver. Our excellence is defined by unwavering quality of work, attention to detail, consistent/timely communications, flexibility to change, and through fair and reasonable pricing. Ultimately, it is our commitment to these values that result in anticipating and exceeding our clients expectations.</p>
    </section>
  </main>

  <p class="copyright">COPYRIGHT (C) 2012 K&amp;V MEDLINK COMMUNICATIONS</p>

  <footer class="site-footer">
    <span>HOME</span><span>|</span><span>ABOUT</span><span>|</span><span>PRIVACY STATEMENT</span><span>|</span><span>TERMS OF USE</span>
  </footer>
</body>
</html>
```